Business Card Design with new logo

Dorian Pelleway 4172
E 118th St Marrowdale, XZ 00420
Cell: 999-555-0193
pellewayrestoration@mailvane.test

Classic Car Restoration Services Buy Sell Trade Consign

Dorian Pelleway 9698
Cell: 999-555-0193

```html
<!DOCTYPE html>
<html lang="en">
<head>
<meta charset="utf-8">
<title>Pelleway Restoration – Business Card</title>
<link href="https://fonts.googleapis.com/css2?family=Lato:wght@300;400&family=Montserrat:wght@500;700&display=swap" rel="stylesheet">
<style>
  :root{
    --bg:#e6eaea;
    --card:#ffffff;
    --red:#e0151f;
    --navy:#1d2430;
    --ink:#1e2330;
    --faint:rgba(224,21,31,0.09);
  }
  *{box-sizing:border-box;margin:0;padding:0}
  html,body{width:1200px;height:1200px;overflow:hidden;background:var(--bg)}
  .canvas{position:relative;width:1200px;height:1200px}
  .card{position:absolute;left:180px;width:840px;height:480px;background:var(--card);
        border-radius:34px;overflow:hidden;box-shadow:0 14px 30px rgba(0,0,0,.12)}
  .card--back{top:60px}
  .card--front{top:660px}

  /* back side */
  .back-brand{position:absolute;left:0;right:0;top:150px;text-align:center;
        font-family:"Montserrat",sans-serif;font-weight:700;font-size:46px;color:var(--red);letter-spacing:1px}
  .back-band{position:absolute;left:0;right:0;bottom:0;height:78px;
        background:linear-gradient(90deg,#3a4452,var(--navy) 30%,var(--navy))}
  .back-tab{position:absolute;left:370px;bottom:64px;width:110px;height:28px;background:var(--red);
        clip-path:polygon(12% 0,88% 0,100% 100%,0 100%)}

  /* front side */
  .watermark{position:absolute;right:60px;top:28px;font-family:"Montserrat",sans-serif;
        font-weight:700;font-size:54px;color:var(--faint)}
  .brand{position:absolute;left:62px;top:110px;display:flex;align-items:center;gap:12px}
  .brand-dot{width:18px;height:18px;border-radius:50%;background:var(--red)}
  .brand-name{font-family:"Montserrat",sans-serif;font-weight:700;font-size:26px;color:var(--navy);line-height:1.2}
  .tagline{position:absolute;left:0;top:250px;width:520px;height:46px;background:var(--red);
        clip-path:polygon(0 0,97% 0,100% 100%,0 100%);
        font-family:"Lato",sans-serif;font-weight:300;font-size:26px;color:#fff;letter-spacing:1.5px;
        padding:7px 0 0 80px}
  .services{position:absolute;left:95px;top:312px;display:flex;gap:22px;
        font-family:"Lato",sans-serif;font-size:22px;color:var(--ink)}
  .services span{display:flex;align-items:center;gap:5px}
  .services svg{width:16px;height:16px}

  .contact{position:absolute;left:450px;top:110px;font-family:"Montserrat",sans-serif;
        font-weight:500;font-size:20px;color:var(--ink);line-height:1.25}
  .contact-row{display:flex;align-items:flex-start;gap:10px;margin-bottom:14px}
  .contact-icon{width:24px;height:24px;flex:none;margin-top:1px}
  .contact-rule{width:1.5px;height:26px;background:var(--red);flex:none}
  .contact-rule--tall{height:50px}
  .contact-email{font-size:18px}

  .foot-red{position:absolute;left:400px;right:0;bottom:0;height:50px;background:var(--red);
        border-radius:25px 0 0 0}
  .foot-navy{position:absolute;right:0;bottom:0;width:110px;height:110px;background:var(--navy);
        border-radius:36px 0 0 0}
</style>
</head>
<body>
<main class="canvas">

  <section class="card card--back" aria-label="Card back">
    <div class="back-brand">Pelleway Restoration</div>
    <div class="back-band"></div>
    <div class="back-tab"></div>
  </section>

  <section class="card card--front" aria-label="Card front">
    <div class="watermark" aria-hidden="true">Pelleway</div>

    <div class="brand">
      <span class="brand-dot"></span>
      <span class="brand-name">Pelleway<br>Restoration LLC</span>
    </div>

    <div class="tagline">Classic Car Restoration</div>
    <div class="services">
      <span><svg viewBox="0 0 16 16"><path d="M2 9l4 4 8-11" fill="none" stroke="#e0151f" stroke-width="2.6" stroke-linecap="round"/></svg>Buy</span>
      <span><svg viewBox="0 0 16 16"><path d="M2 9l4 4 8-11" fill="none" stroke="#e0151f" stroke-width="2.6" stroke-linecap="round"/></svg>Sell</span>
      <span><svg viewBox="0 0 16 16"><path d="M2 9l4 4 8-11" fill="none" stroke="#e0151f" stroke-width="2.6" stroke-linecap="round"/></svg>Trade</span>
      <span><svg viewBox="0 0 16 16"><path d="M2 9l4 4 8-11" fill="none" stroke="#e0151f" stroke-width="2.6" stroke-linecap="round"/></svg>Consign</span>
    </div>

    <div class="contact">
      <div class="contact-row">
        <svg class="contact-icon" viewBox="0 0 24 24"><path d="M6 3l3 4-2 2c1 3 4 6 7 7l2-2 4 3-2 3C10 20 4 14 3 5z" fill="none" stroke="#e0151f" stroke-width="1.6" stroke-linejoin="round"/></svg>
        <span class="contact-rule"></span><span>999-555-0193</span>
      </div>
      <div class="contact-row">
        <svg class="contact-icon" viewBox="0 0 24 24"><rect x="6" y="3" width="12" height="18" rx="6" fill="none" stroke="#e0151f" stroke-width="1.6"/><line x1="12" y1="7" x2="12" y2="11" stroke="#e0151f" stroke-width="1.6"/></svg>
        <span class="contact-rule"></span><span class="contact-email">pellewayrestoration@mailvane.test</span>
      </div>
      <div class="contact-row">
        <svg class="contact-icon" viewBox="0 0 24 24"><path d="M12 22s-7-7-7-12a7 7 0 0 1 14 0c0 5-7 12-7 12z" fill="none" stroke="#e0151f" stroke-width="1.6"/><circle cx="12" cy="10" r="2.5" fill="none" stroke="#e0151f" stroke-width="1.6"/></svg>
        <span class="contact-rule contact-rule--tall"></span><span>Dorian Pelleway 4172<br>E 118th St Marrowdale, XZ 00420</span>
      </div>
    </div>

    <div class="foot-red"></div>
    <div class="foot-navy"></div>
  </section>

</main>
</body>
</html>
```